Hip-Hop Artist MK Drift new album cover design for "Hollow Marigold"

Artist: MK Drift
Album Title: Hollow Marigold
I am attaching a un-edited picture to use & some sample images with the "Hollow Marigold" concept directions. I am hoping that the graphic designers accepting this challenge can do a better or different job than the 3 sample design images attached. I do like each of the 3 attached drafts(Draft, Draft2, Draft3) concepts. But, would like to see other creative design approaches and other possible affect. artwork ideas.
I am also attaching a number of random design that I also like the direction on.
Please let em know if you have any questions, and I will respond as quickly as possible.

```html
<!DOCTYPE html>
<html lang="en">
<head>
<meta charset="utf-8">
<title>MK Drift — Hollow Marigold</title>
<link href="https://fonts.googleapis.com/css2?family=Josefin+Sans:wght@300&family=Cinzel:wght@400&display=swap" rel="stylesheet">
<style>
  :root {
    --floor-dark: #2a1f1c;
    --floor-warm: #6b3320;
    --paper: #e9e4e4;
    --figure: #141010;
    --block-wine: rgba(110, 8, 8, 0.62);
    --block-night: rgba(25, 0, 0, 0.78);
    --block-ash: rgba(30, 30, 28, 0.82);
    --block-slate: rgba(70, 70, 68, 0.55);
    --block-blush: rgba(255, 225, 228, 0.35);
    --block-ember: rgba(120, 10, 10, 0.45);
    --title: #ffffff;
    --title-ghost: rgba(30, 20, 20, 0.45);
    --name-band: #5a0d0d;
    --name: #f4eeee;
  }
  html, body {
    margin: 0;
    padding: 0;
    width: 1200px;
    height: 1108px;
    overflow: hidden;
    background: #111;
  }
  .cover {
    display: block;
    width: 1200px;
    height: 1108px;
  }
  .title {
    font-family: "Josefin Sans", "Century Gothic", sans-serif;
    font-weight: 300;
    font-size: 238px;
  }
  .title--main { fill: var(--title); }
  .title--ghost { fill: var(--title-ghost); }
  .artist-name {
    font-family: "Cinzel", "Trajan Pro", serif;
    font-size: 58px;
    fill: var(--name);
  }
</style>
</head>
<body>
<svg class="cover" viewBox="0 0 1200 1108" xmlns="http://www.w3.org/2000/svg">
  <defs>
    <linearGradient id="floorTone" x1="0" y1="0" x2="1" y2="1">
      <stop offset="0" stop-color="var(--floor-dark)"/>
      <stop offset="0.6" stop-color="#3a2a24"/>
      <stop offset="1" stop-color="var(--floor-warm)"/>
    </linearGradient>
    <radialGradient id="paperSpread" cx="0.5" cy="0.62" r="0.42">
      <stop offset="0" stop-color="var(--paper)"/>
      <stop offset="0.75" stop-color="var(--paper)" stop-opacity="0.85"/>
      <stop offset="1" stop-color="var(--paper)" stop-opacity="0"/>
    </radialGradient>
    <linearGradient id="figureTone" x1="0" y1="0" x2="0" y2="1">
      <stop offset="0" stop-color="var(--figure)"/>
      <stop offset="1" stop-color="#2a2424"/>
    </linearGradient>
  </defs>

  <g class="cover-photo" role="img" aria-label="Overhead photograph of the artist crouching in a dark shirt and sneakers on a wooden floor, surrounded by a circle of scattered lyric sheets">
    <rect width="1200" height="1108" fill="url(#floorTone)"/>
    <rect width="1200" height="1108" fill="url(#paperSpread)"/>
    <rect x="400" y="90" width="400" height="780" rx="120" fill="url(#figureTone)" opacity="0.85"/>
  </g>

  <g class="color-blocks">
    <rect x="0" y="0" width="400" height="554" fill="var(--block-wine)"/>
    <rect x="400" y="0" width="400" height="554" fill="var(--block-night)"/>
    <rect x="800" y="0" width="400" height="554" fill="var(--block-ash)"/>
    <rect x="0" y="554" width="400" height="554" fill="var(--block-slate)"/>
    <rect x="400" y="554" width="400" height="554" fill="var(--block-blush)"/>
    <rect x="800" y="554" width="400" height="554" fill="var(--block-ember)"/>
  </g>

  <g class="album-title">
    <text class="title title--ghost" x="170" y="556" textLength="870" lengthAdjust="spacingAndGlyphs">HOLLOW</text>
    <text class="title title--ghost" x="8" y="752" textLength="1110" lengthAdjust="spacingAndGlyphs">MARIGOLD</text>
    <text class="title title--main" x="212" y="544" textLength="828" lengthAdjust="spacingAndGlyphs">HOLLOW</text>
    <text class="title title--main" x="44" y="740" textLength="1108" lengthAdjust="spacingAndGlyphs">MARIGOLD</text>
  </g>

  <g class="artist">
    <rect x="462" y="1024" width="286" height="50" fill="var(--name-band)" opacity="0.85"/>
    <text class="artist-name" x="606" y="1080" text-anchor="middle" textLength="276" lengthAdjust="spacingAndGlyphs">MK DRIFT</text>
  </g>
</svg>
</body>
</html>
```